Solvanta Clinica Business Card Design and print

I have attached the design I require including JPEG for company logo. I would like a copy of the art work for future needs.

Double sided - the item will not change from single

250 cards with both names on Ruth Calloway and Megan Thorpe

250 cards with Ruth Calloway only

Industry/Entity Type

Business

Contact Information for Business Card

See attached layout

```html
<!DOCTYPE html>
<html lang="en">
<head>
<meta charset="utf-8">
<title>Solvanta Clinica – Business Card</title>
<link rel="stylesheet" href="https://fonts.googleapis.com/css2?family=Lato:wght@300;400;700&display=swap">
<style>
  :root {
    --backdrop: #e6e6e9;
    --brand-purple: #824c9f;
    --brand-orange: #e07a24;
    --card-white: #ffffff;
    --text-on-purple: #ffffff;
    --card-shadow: 0 10px 24px rgba(0, 0, 0, 0.14);
  }
  * { box-sizing: border-box; margin: 0; padding: 0; }
  html, body {
    width: 1200px;
    height: 800px;
    overflow: hidden;
    background: var(--backdrop);
    font-family: "Lato", sans-serif;
  }
  .canvas {
    position: relative;
    width: 1200px;
    height: 800px;
    display: flex;
    align-items: center;
    justify-content: center;
    gap: 60px;
  }
  .card {
    position: relative;
    width: 520px;
    height: 318px;
    box-shadow: var(--card-shadow);
    overflow: hidden;
  }

  /* Front side */
  .card-front {
    background: var(--brand-purple);
    color: var(--text-on-purple);
    display: flex;
    flex-direction: column;
    align-items: center;
    justify-content: center;
  }
  .wordmark {
    display: flex;
    align-items: center;
    gap: 12px;
    font-weight: 300;
    font-size: 32px;
    letter-spacing: 0.5px;
    text-transform: lowercase;
  }
  .wordmark-square {
    width: 30px;
    height: 30px;
    background: var(--text-on-purple);
  }
  .front-url {
    margin-top: 26px;
    font-size: 12px;
    font-weight: 400;
    letter-spacing: 0.3px;
  }

  /* Back side */
  .card-back {
    background: var(--card-white);
  }
  .back-brand {
    position: absolute;
    left: 34px;
    top: 50%;
    transform: translateY(-50%);
    display: flex;
    align-items: center;
    gap: 10px;
    color: var(--brand-orange);
    font-weight: 400;
    font-size: 22px;
    text-transform: lowercase;
  }
  .back-brand-square {
    width: 22px;
    height: 22px;
    background: var(--brand-orange);
  }
  .contact-panel {
    position: absolute;
    left: 300px;
    top: 40px;
    width: 196px;
    height: 250px;
    background: var(--brand-purple);
    color: var(--text-on-purple);
    padding: 30px 16px 0 22px;
    font-size: 10.5px;
    line-height: 1.45;
  }
  .contact-person + .contact-person { margin-top: 6px; }
  .contact-name {
    font-weight: 700;
    font-size: 14px;
    line-height: 1.3;
  }
  .contact-web { margin-top: 14px; }
</style>
</head>
<body>
  <main class="canvas">
    <section class="card card-front" aria-label="Card front">
      <div class="wordmark">
        <span class="wordmark-square" aria-hidden="true"></span>
        <span class="wordmark-name">solvanta clinica</span>
      </div>
      <p class="front-url">www.solvantaclinica.com.au</p>
    </section>

    <section class="card card-back" aria-label="Card back">
      <div class="back-brand">
        <span class="back-brand-name">solvanta clinica</span>
        <span class="back-brand-square" aria-hidden="true"></span>
      </div>
      <div class="contact-panel">
        <div class="contact-person">
          <p class="contact-name">Ruth Calloway</p>
          <p>ruth@solvantaclinica.com.au</p>
          <p>+61 (0)400 318 274</p>
        </div>
        <div class="contact-person">
          <p class="contact-name">Megan Thorpe</p>
          <p>megan@solvantaclinica.com.au</p>
          <p>+61 (0)400 762 159</p>
        </div>
        <p class="contact-web">www.solvantaclinica.com.au</p>
      </div>
    </section>
  </main>
</body>
</html>
```